Venture Capital Investment Firm

We are looking to overhaul our existing website (substantially), with only using the same logos (which we can provide).
We are an investment firm that focuses on making loans to late stage technology companies. Our site should ultimately look like other venture capital firms, and look modern and fresh. We have an existing website www.northvaleloan.com which this will be replacing, although we will be using a lot of the existing written content, and potentially the numbers of pages we will need, we are not wed to anything else. Please feel free to shoot any questions at any time and thank you in advance for your help!
Websites we like as examples:
https://www.tkbrandel.com/
https://www.emberwoodfunds.com/
Target Market(s)
Potential investors who will invest in our firm, as well as potentially companies that are looking to borrow money from us.

```html
<!DOCTYPE html>
<html lang="en">
<head>
<meta charset="utf-8">
<title>Northvale Investment Partners</title>
<link rel="stylesheet" href="https://fonts.googleapis.com/css2?family=Roboto:wght@300;400&display=swap">
<style>
:root{
  --navy:#121d2b;
  --night-top:#1c2530;
  --night-bottom:#0b0f15;
  --yellow:#f4e24a;
  --white:#ffffff;
  --ink:#1d2733;
  --mist:#e6e6e6;
  --photo:#1a1a1a;
  --photo-light:#6b6b6b;
}
*{margin:0;padding:0;box-sizing:border-box}
html,body{width:703px;height:1200px;overflow:hidden}
body{position:relative;font-family:"Roboto",sans-serif;font-weight:300;background:var(--white);color:var(--ink)}
.hero{position:absolute;left:0;top:0;width:703px;height:401px;overflow:hidden}
.hero-backdrop{position:absolute;inset:0;background:radial-gradient(ellipse at 70% 15%,#3a4452 0%,transparent 55%),linear-gradient(180deg,var(--night-top) 0%,#141a22 55%,var(--night-bottom) 100%)}
.site-mark{position:absolute;left:18px;top:15px;display:flex;align-items:center;gap:7px;color:var(--white);font-size:20px;font-weight:400;letter-spacing:1px}
.site-mark .dot{width:14px;height:14px;border-radius:50%;background:var(--white)}
.main-nav{position:absolute;top:20px;left:0;width:703px;height:20px}
.main-nav a{position:absolute;color:var(--white);text-decoration:none;font-size:14.5px;font-weight:300}
.main-nav a.current{color:var(--yellow)}
.hero-name{position:absolute;left:0;width:703px;top:128px;text-align:center;color:var(--white)}
.hero-name .firm{display:block;font-size:32px;font-weight:400;letter-spacing:2px}
.hero-name .entity{display:block;font-size:9px;font-weight:400;letter-spacing:1px;margin-top:2px}
.tagline{position:absolute;left:0;width:703px;top:198px;text-align:center;color:var(--white);font-size:11.5px;line-height:15px;font-weight:300}
.cta{position:absolute;left:269px;top:239px;width:172px;height:23px;border:1px solid var(--yellow);border-radius:12px;color:var(--yellow);font-size:17px;line-height:21px;text-align:center;text-decoration:none}
.focus{position:absolute;left:0;top:401px;width:703px;height:139px;background:var(--navy)}
.focus-text{position:absolute;left:18px;top:10px;width:400px;color:var(--white);font-size:13px;line-height:17px}
.focus-link{position:absolute;left:440px;top:42px;width:150px;text-align:center;color:var(--yellow);font-size:18px;line-height:24px;text-decoration:none}
.team{position:absolute;left:0;top:540px;width:703px;height:250px}
.section-title{position:absolute;font-size:18px;font-weight:300;color:var(--ink)}
.team .section-title{left:27px;top:14px}
.arrows{color:var(--yellow);font-size:12px;margin-left:8px;letter-spacing:-2px}
.member{position:absolute;top:51px;width:161px;text-align:center}
.portrait{width:161px;height:161px;background:radial-gradient(circle at 50% 40%,var(--photo-light) 0%,var(--photo) 60%)}
.member-name{display:block;margin-top:5px;font-size:18px;color:var(--ink)}
.contact{position:absolute;left:0;top:790px;width:703px;height:319px;background:var(--mist)}
.contact .section-title{left:28px;top:20px;font-size:21px}
.inquiry{position:absolute;left:18px;font-size:14px;line-height:18px;color:var(--ink)}
.inquiry span{display:block}
.map{position:absolute;left:311px;top:60px;width:346px;height:230px;background:linear-gradient(160deg,#d5e8c9 0%,#aed4f4 35%,#aad2f5 60%,#dce6cf 100%)}
.footer{position:absolute;left:0;top:1109px;width:703px;height:91px;background:var(--navy);text-align:center}
.footer-name{position:absolute;left:0;width:703px;top:18px;color:var(--yellow);font-size:13px}
.footer-legal{position:absolute;left:0;width:703px;top:43px;color:var(--white);font-size:9px}
.footer-legal span{margin-left:16px}
</style>
</head>
<body>
<header class="hero">
  <div class="hero-backdrop" role="img" aria-label="Night city skyline with star trails"></div>
  <div class="site-mark"><span class="dot"></span>NORTHVALE</div>
  <nav class="main-nav">
    <a class="current" style="left:306px" href="#">Home</a>
    <a style="left:364px" href="#">Strategy</a>
    <a style="left:439px" href="#">About Us</a>
    <a style="left:519px" href="#">Team</a>
    <a style="left:575px" href="#">News</a>
    <a style="left:632px" href="#">Investors</a>
  </nav>
  <div class="hero-name"><span class="firm">NORTHVALE</span><span class="entity">INVESTMENT PARTNERS, LLC</span></div>
  <p class="tagline">WE ARE A GLOBAL STRUCTURED CREDIT INVESTMENT FIRM FOCUSED ON THE<br>HEALTHCARE AND TECHNOLOGY INDUSTRIES</p>
  <a class="cta" href="#">Contact us</a>
</header>

<section class="focus">
  <p class="focus-text">Our focus spans the life science and technology industries, two sectors where intellectual property (IP) is an integral driver of asset and enterprise value. Our broad experience in investing, technology evaluation, and product forecasting affords us a unique understanding of the value of assets in these dynamic sectors, allowing us to see value where others cannot.</p>
  <a class="focus-link" href="#">Learn about our strategy <span class="arrows">▶▶</span></a>
</section>

<section class="team">
  <h2 class="section-title">MEET OUR TEAM<span class="arrows">▶▶</span></h2>
  <div class="member" style="left:51px"><div class="portrait" role="img" aria-label="Black and white portrait of Marcus Ellery"></div><span class="member-name">Marcus Ellery</span></div>
  <div class="member" style="left:272px"><div class="portrait" role="img" aria-label="Black and white portrait of Devan Kapoor"></div><span class="member-name">Devan Kapoor</span></div>
  <div class="member" style="left:492px"><div class="portrait" role="img" aria-label="Black and white portrait of Owen Hartley"></div><span class="member-name">Owen Hartley</span></div>
</section>

<section class="contact">
  <h2 class="section-title">Contact Us</h2>
  <p class="inquiry" style="top:72px"><span>GENERAL INQUIRIES</span><span>Please write to:&nbsp; inquiries@northvaleloan.com</span></p>
  <p class="inquiry" style="top:125px"><span>TRANSACTION OPPORTUNITIES</span><span>Please write to:&nbsp; invopps@northvaleloan.com</span></p>
  <p class="inquiry" style="top:176px"><span>MEDIA INQUIRIES</span><span>Please write to:&nbsp; media@northvaleloan.com</span></p>
  <p class="inquiry" style="top:229px"><span>CAREERS</span><span>Please write to:&nbsp; career@northvaleloan.com</span></p>
  <div class="map" role="img" aria-label="Map of the San Francisco Bay Area with the office location marked"></div>
</section>

<footer class="footer">
  <p class="footer-name">NORTHVALE, SAN FRANCISCO</p>
  <p class="footer-legal">© 2015 Northvale Investment Partners LLC.&nbsp; All Rights Reserved.<span>Legal Disclaimer</span></p>
</footer>
</body>
</html>
```